Real estate agent : TJ Property

I have done the attached logo designed by your company .
My business card description as below:
Name : Daniel Ruiz
Mobile: 0491570156
Email : danielr@tjpropertyhq.net.au
Sales & Property Management

```html
<!DOCTYPE html>
<html lang="en">
<head>
<meta charset="utf-8">
<title>TJ Property – Business Card</title>
<link rel="stylesheet" href="https://fonts.googleapis.com/css2?family=Montserrat:wght@400;500;700;800&display=swap">
<style>
  :root {
    --backdrop: #1b1b1b;
    --card: #2d2d2d;
    --ink-light: #ffffff;
    --ink-muted: #d9d9d9;
    --ink-dark: #0f0f0f;
    --rule: #8a8a8a;
  }
  * { box-sizing: border-box; margin: 0; padding: 0; }
  html, body {
    width: 1200px;
    height: 1186px;
    overflow: hidden;
    background: var(--backdrop);
    font-family: "Montserrat", sans-serif;
  }
  .stage {
    position: relative;
    width: 1200px;
    height: 1186px;
  }
  .card {
    position: absolute;
    width: 760px;
    height: 434px;
    background: var(--card);
    border-radius: 30px;
    overflow: hidden;
  }
  .card--front { left: 60px; top: 70px; }
  .card--back { left: 380px; top: 650px; }

  .brand-front {
    position: absolute;
    inset: 0;
    display: flex;
    align-items: center;
    justify-content: center;
    gap: 22px;
  }
  .brand-front .brand-mark {
    width: 46px;
    height: 46px;
    background: var(--ink-dark);
  }
  .brand-front .brand-name {
    font-weight: 800;
    font-size: 78px;
    letter-spacing: 1px;
    color: var(--ink-dark);
  }

  .brand-back {
    position: absolute;
    right: 60px;
    top: 70px;
    display: flex;
    align-items: center;
    gap: 14px;
  }
  .brand-back .brand-mark {
    width: 26px;
    height: 26px;
    background: var(--ink-light);
  }
  .brand-back .brand-name {
    font-weight: 800;
    font-size: 44px;
    color: var(--ink-light);
  }
  .divider-top {
    position: absolute;
    left: 360px;
    right: 40px;
    top: 160px;
    height: 1px;
    background: var(--rule);
  }
  .contact {
    position: absolute;
    left: 46px;
    bottom: 44px;
    width: 340px;
  }
  .contact-name {
    font-weight: 700;
    font-size: 28px;
    color: var(--ink-light);
    padding-bottom: 12px;
    border-bottom: 1px solid var(--rule);
    margin-bottom: 14px;
  }
  .contact-line {
    display: flex;
    align-items: center;
    gap: 14px;
    font-weight: 400;
    font-size: 17px;
    color: var(--ink-muted);
    margin-bottom: 10px;
  }
  .contact-line svg {
    width: 16px;
    height: 16px;
    fill: var(--ink-light);
    flex: none;
  }
</style>
</head>
<body>
<main class="stage">
  <section class="card card--front" aria-label="Card front">
    <div class="brand-front">
      <span class="brand-mark"></span>
      <span class="brand-name">TJ Property</span>
    </div>
  </section>

  <section class="card card--back" aria-label="Card back">
    <div class="brand-back">
      <span class="brand-mark"></span>
      <span class="brand-name">TJ Property</span>
    </div>
    <div class="divider-top"></div>
    <div class="contact">
      <p class="contact-name">Daniel Ruiz</p>
      <p class="contact-line">
        <svg viewBox="0 0 24 24" aria-hidden="true"><path d="M6.6 10.8a15.1 15.1 0 0 0 6.6 6.6l2.2-2.2a1 1 0 0 1 1-.25 11.4 11.4 0 0 0 3.6.57 1 1 0 0 1 1 1V20a1 1 0 0 1-1 1A17 17 0 0 1 3 4a1 1 0 0 1 1-1h3.5a1 1 0 0 1 1 1c0 1.25.2 2.45.57 3.57a1 1 0 0 1-.25 1z"/></svg>
        <span>0491570156</span>
      </p>
      <p class="contact-line">
        <svg viewBox="0 0 24 24" aria-hidden="true"><path d="M2 5h20v14H2zm2 2v.5l8 5 8-5V7l-8 5z"/></svg>
        <span>danielr@tjpropertyhq.net.au</span>
      </p>
    </div>
  </section>
</main>
</body>
</html>
```